Improved Business Card, Government Contracting

We are looking to update the design of our business cards. We would like to create a template that can be used for future employees and easy to update.

Haldecott Advisory Partners, LLC is a Service Disabled Veteran Owned Small Business with headquarters located in Leavenworth, KS. Our current website is www.hdvprt.example. We have contracts in KS and VA with expansion opportunities in various other states. Our primary line of work is within government contracting and providing consulting services to various organizations within the Bureau of Civic Readiness. We would like to project a professional image of our company that is consistent with the industry. Provided are previous versions of our business card template that shows our logo as well. We would like to make sure the information on the cards are easily noticeable .

Target Market(s)

Government Officials
Fellow Small Business Contractors
Large Business Contractors (ex. TQRB, Vellacourt Dynamics, Crest Pallow Wendry)

Industry/Entity Type

Business

Contact Information for Business Card

Paul Larkin
Office Manager
Haldecott Advisory Partners
Ph: 555.014.2738
Email: p.larkin@hdvprt.example
www.hdvprt.example

Requirements
Must have
• The business mailing address is:
• 48312 902nd Crossing
• Leavenworth, KS 00000
Nice to have
• Embossed lettering

```html
<!DOCTYPE html>
<html lang="en">
<head>
<meta charset="utf-8">
<title>Haldecott Advisory Partners — Business Card</title>
<link rel="stylesheet" href="https://fonts.googleapis.com/css2?family=Jost:ital,wght@0,400;0,500;0,700;1,400&display=swap">
<style>
  :root {
    --brand-blue: #3d5ca8;
    --brand-gold: #fcc40c;
    --paper: #ffffff;
    --ink-light: #ffffff;
  }
  html, body {
    margin: 0;
    padding: 0;
    overflow: hidden;
    background: var(--paper);
  }
  .card {
    position: relative;
    width: 1200px;
    height: 683px;
    overflow: hidden;
    background: var(--paper);
    font-family: "Jost", sans-serif;
  }
  .card-backdrop {
    position: absolute;
    inset: 0;
    width: 1200px;
    height: 683px;
  }
  .card-backdrop .field { fill: var(--brand-blue); }

  .brand-name {
    position: absolute;
    left: 145px;
    top: 158px;
    width: 600px;
    margin: 0;
    text-align: center;
    color: var(--brand-blue);
    font-weight: 500;
    font-size: 46px;
    line-height: 54px;
    letter-spacing: 2px;
    text-transform: uppercase;
  }

  .holder {
    position: absolute;
    left: 60px;
    top: 462px;
  }
  .holder-name {
    margin: 0;
    color: var(--brand-gold);
    font-weight: 700;
    font-size: 48px;
    line-height: 56px;
  }
  .holder-title {
    margin: 0;
    color: var(--brand-gold);
    font-style: italic;
    font-weight: 400;
    font-size: 32px;
    line-height: 40px;
  }

  .mailing {
    position: absolute;
    left: 60px;
    top: 590px;
    margin: 0;
    color: var(--ink-light);
    font-style: normal;
    font-weight: 400;
    font-size: 24px;
    line-height: 32px;
    letter-spacing: 0.5px;
  }

  .contact {
    position: absolute;
    left: 683px;
    top: 478px;
    margin: 0;
    color: var(--ink-light);
    font-style: normal;
    font-size: 32px;
    line-height: 48px;
  }
  .contact-row { display: flex; margin: 0; }
  .contact-label {
    width: 67px;
    font-weight: 700;
  }
  .contact-value { font-weight: 400; letter-spacing: 0.5px; }
  .contact-web {
    margin: 0;
    font-weight: 700;
    letter-spacing: 0.5px;
  }
</style>
</head>
<body>
<main class="card">
  <svg class="card-backdrop" viewBox="0 0 1200 683" aria-hidden="true">
    <polygon class="field" points="0,262 445,452 1200,130 1200,683 0,683"/>
  </svg>

  <h1 class="brand-name">Haldecott<br>Advisory Partners</h1>

  <section class="holder">
    <p class="holder-name">Paul Larkin</p>
    <p class="holder-title">Office Manager</p>
  </section>

  <address class="mailing">48312 902nd Crossing<br>Leavenworth, KS 00000</address>

  <address class="contact">
    <p class="contact-row"><span class="contact-label">P:</span><span class="contact-value">555.014.2738</span></p>
    <p class="contact-row"><span class="contact-label">E:</span><span class="contact-value">p.larkin@hdvprt.example</span></p>
    <p class="contact-web">www.hdvprt.example</p>
  </address>
</main>
</body>
</html>
```